MS Word Template needed for a company specialized in Insurance and Finance Advising

I am looking for an impressive and memorable Word Template for:

Writing daily letters
Presentations
Agreements
Front Pages for Projects
Finance, pension, tax analyzes ...

Our logo is attached.
We are advising clients in all kind of questions in the finance and insurance industry, we are not selling products, our main business is the advising and to win the trust to all kind of costumers, from young to old from all kind of nations.

```html
<!DOCTYPE html>
<html lang="en">
<head>
<meta charset="utf-8">
<title>Alpen Counsel – Word Template Set</title>
<link rel="stylesheet" href="https://fonts.googleapis.com/css2?family=Open+Sans:wght@400;600;700&family=Roboto:wght@400;700&family=Share+Tech+Mono&display=swap">
<style>
  :root{
    --board:#d6d6d6;
    --paper:#ffffff;
    --red:#e02026;
    --red-deep:#b8141a;
    --grey:#8e8f93;
    --grey-dark:#5e5f62;
    --ink:#222222;
    --ink-soft:#8a8a8a;
    --map:#e4e4e4;
    --night:#16181b;
  }
  *{box-sizing:border-box;margin:0;padding:0}
  html,body{width:935px;height:1200px;overflow:hidden;background:var(--board)}
  body{position:relative;font-family:"Open Sans",Arial,sans-serif;color:var(--ink)}
  .page{position:absolute;width:297px;height:385px;background:var(--paper);overflow:hidden;box-shadow:0 0 0 .5px #9a9a9a}
  .abs{position:absolute}
  .body-copy{font-size:3.6px;line-height:5.3px;text-align:justify}
  .body-copy p{margin-bottom:5px}
  .brand{font-family:"Open Sans",Arial,sans-serif;font-weight:700;letter-spacing:.5px;color:var(--red);white-space:nowrap}
  .brand.on-dark{color:#fff}
  .map-band{position:absolute;left:0;width:100%;background:linear-gradient(180deg,#ececec,#f7f7f7)}
  .contact-list{font-size:4px;line-height:6px;color:var(--ink-soft)}
  .hex-title{position:absolute;z-index:2;font-family:"Roboto",Arial,sans-serif;font-size:25px;line-height:1;letter-spacing:.3px;white-space:nowrap}
  .hex-title b{color:var(--red);font-weight:700}
  .hex-title span{color:var(--grey);font-weight:400}
  .promo{position:absolute;left:440px;top:900px;width:420px;text-align:center}
  .promo .brand{font-size:34px;letter-spacing:2px;margin-bottom:10px}
  .promo-line{font-family:"Share Tech Mono",monospace;font-size:17px;line-height:19.5px;color:var(--ink);letter-spacing:1.5px}
</style>
</head>
<body>

<!-- Letterhead -->
<section class="page" style="left:10px;top:9px">
  <svg class="abs" style="left:0;top:0" width="297" height="385" viewBox="0 0 297 385">
    <polygon points="78,13 122,13 128,21 84,21" fill="var(--grey)"/>
    <polygon points="122,13 297,13 297,21 128,21" fill="var(--red)"/>
    <polygon points="0,310 297,357 297,385 0,385" fill="var(--night)"/>
    <polygon points="0,310 297,357 297,364 0,317" fill="var(--red)"/>
    <polygon points="178,339 297,317 297,362" fill="var(--red)"/>
  </svg>
  <div class="brand abs" style="left:8px;top:12px;font-size:7.5px">ALPEN COUNSEL</div>
  <div class="abs" style="left:14px;top:46px;font-size:3.6px;line-height:5px;width:270px">
    <p>Month 01, 2020</p>
    <p style="margin-top:5px;font-weight:600">Company Name</p>
    <p style="padding-left:10px">Address Line 1</p>
    <p style="padding-left:10px">Address Line 2</p>
    <p style="margin-top:9px">[To Whom it may concern];</p>
    <div class="body-copy" style="margin-top:5px;text-indent:14px">
      <p>Lorem ipsum dolor sit amet, consectetur adipiscing elit. Phasellus et sollicitudin purus, vel blandit libero. Fusce vitae tempor diam, a semper orci. In eget nisl tellus. Vivamus diam dolor, porta eget ex nec, suscipit finibus sem. Donec ut purus dictum, efficitur ipsum non, facilisis arcu. Aliquam nunc elit, efficitur non ligula a, feugiat condimentum nunc. Etiam maximus est quis erat suscipit auctor. Pellentesque habitant morbi tristique senectus et netus et malesuada fames ac turpis egestas. Mauris a condimentum orci, non fermentum dui. Maecenas ornare metus ipsum, mollis dignissim nulla lobortis quis.</p>
      <p style="margin-top:9px">Pellentesque id dolor fringilla, semper diam vitae, pulvinar massa. Etiam vitae vulputate urna, vel fringilla ante. Sed et arcu a nulla finibus consequat. Vestibulum facilisis ligula ac ultricies convallis. Curabitur imperdiet augue odio, sed varius lacus gravida quis. Duis ullamcorper ullamcorper libero, eu iaculis urna gravida vel. Mauris condimentum diam et nibh eleifend, sit amet faucibus tortor mollis. Lorem ipsum dolor sit amet, consectetur adipiscing elit.</p>
      <p>Integer ut fermentum neque. Phasellus sapien turpis, ultricies ac turpis vel, placerat porttitor odio. Donec ut dapibus eros, ac malesuada arcu. Nam tincidunt lacus in rutrum convallis. Quisque blandit leo id velit malesuada, ut lobortis dui mollis.</p>
      <p>Aliquam ultricies elementum leo a efficitur. Vestibulum tellus purus, faucibus in neque id, faucibus pretium ligula. Proin commodo est sapien, sit amet sodales odio lacinia et. Etiam malesuada sapien ut varius dictum. Suspendisse interdum nec nisl vitae blandit.</p>
      <p>Praesent at felis euismod, iaculis justo nec, elementum erat. Suspendisse nisl quam, condimentum ut viverra laoreet, cursus et nisi. Vestibulum accumsan a arcu at aliquam. Sed tincidunt pulvinar felis, accumsan sollicitudin velit posuere eget. Donec vulputate auctor mattis.</p>
    </div>
    <p style="margin-top:3px">Best,<br>[Your Name]</p>
  </div>
  <svg class="abs" style="left:22px;top:340px" width="10" height="44" viewBox="0 0 10 44" fill="#fff">
    <path d="M2 1c1 0 2 2 2 2l-1 1c0 1 1 2 2 2l1-1s2 1 2 2c0 1-1 1-2 1C4 8 1 5 1 3 1 2 1 1 2 1z"/>
    <circle cx="5" cy="13" r="3" fill="none" stroke="#fff" stroke-width=".7"/>
    <rect x="1.5" y="19" width="7" height="5" fill="none" stroke="#fff" stroke-width=".7"/>
    <path d="M1.5 19l3.5 3 3.5-3" fill="none" stroke="#fff" stroke-width=".6"/>
    <path d="M5 27a2.5 2.5 0 0 1 2.5 2.5C7.5 32 5 35 5 35S2.5 32 2.5 29.5A2.5 2.5 0 0 1 5 27z"/>
  </svg>
  <div class="abs" style="left:35px;top:340px;font-size:4px;line-height:8px;color:#fff">
    000 – 000 – 000<br>www.website.com<br>email@website.com<br>Address Line 1<br>Address Line 2
  </div>
</section>

<!-- Cover page -->
<section class="page" style="left:319px;top:9px;background:#f3f3f3">
  <div class="map-band" role="img" aria-label="Faint dotted world map backdrop" style="top:255px;height:130px;background:linear-gradient(180deg,#e6e6e6,#f5f5f5)"></div>
  <div class="abs" role="img" aria-label="Photo of a smiling couple shaking hands with an advisor at a table" style="left:127px;top:0;width:170px;height:255px;background:linear-gradient(160deg,#c9cdd2 0%,#9aa3ad 45%,#2f3f63 75%,#1d2333 100%)"></div>
  <div class="abs" style="left:12px;top:0;width:115px;height:337px;background:var(--red);color:#fff">
    <div style="position:absolute;left:9px;top:27px;font-size:10.5px;font-weight:600">[Document title]</div>
    <div style="position:absolute;left:9px;top:42px;font-size:7.5px">SUBTITLE</div>
    <div style="position:absolute;left:8px;top:58px;width:52px;height:1.5px;background:#fff"></div>
    <div style="position:absolute;left:11px;top:214px;width:70px;font-size:5.8px">HEADING</div>
    <div style="position:absolute;left:11px;top:222px;width:72px;font-size:4.2px;line-height:5.6px">[Draw your reader in with an engaging abstract. It is typically a short summary of the document.<br>When you're ready to add your content, just click here and start typing.]</div>
    <div style="position:absolute;left:11px;top:286px;font-size:4.2px;font-weight:700">COMPANY NAME</div>
    <div style="position:absolute;left:11px;top:292px;font-size:4.2px">[contact info]</div>
  </div>
  <div class="brand abs" style="right:16px;top:348px;font-size:13px">ALPEN COUNSEL</div>
</section>

<!-- Continuation page -->
<section class="page" style="left:629px;top:9px">
  <div class="map-band" role="img" aria-label="Faint dotted world map band" style="top:0;height:35px"></div>
  <div class="brand abs" style="right:5px;top:14px;font-size:9px">ALPEN COUNSEL</div>
  <div class="body-copy abs" style="left:35px;top:59px;width:227px;font-size:3.9px;line-height:6px">
    <p>Lorem ipsum dolor sit amet, consectetur adipiscing elit. Aenean ullamcorper massa volutpat mauris venenatis, non auctor orci varius. Nulla facilisi. Donec placerat accumsan nisi, ac vulputate tellus dapibus tristique. Phasellus ut purus molestie ex molestie elementum vel sit amet urna. Aenean ex nulla, eleifend feugiat facilisis sit amet, consequat ullamcorper orci. Morbi rhoncus ex sit amet sapien commodo, ut sodales diam rutrum. Sed malesuada tortor eu dignissim eleifend.</p>
    <p>Sed congue sed elit id imperdiet. Vestibulum ante ipsum primis in faucibus orci luctus et ultrices posuere cubilia curae; Sed quam tellus, malesuada non lorem ac, luctus hendrerit arcu. Morbi enim ligula, commodo in arcu ut, mollis luctus nisi. Class aptent taciti sociosqu ad litora torquent per conubia nostra. Duis sollicitudin dui in erat mollis iaculis.</p>
    <p>Aenean molestie, lacus non maximus ultricies, sapien urna eleifend odio, a ullamcorper urna augue molestie purus. Nulla facilisi. Mauris vel commodo mi. Curabitur volutpat orci a tellus maximus rutrum. Ut vulputate mi eu leo luctus, et condimentum enim tincidunt. Nullam viverra consequat nisl et posuere.</p>
    <p>Morbi quis nulla quam. Duis semper accumsan elit, vel ornare nunc facilisis sed. Ut porttitor lorem ut justo mollis pharetra. Sed congue cursus dolor nec dictum. Integer finibus vestibulum pulvinar. Ut sed nulla in nisi fermentum luctus. Pellentesque at aliquam erat.</p>
    <p>Cras at justo a diam faucibus finibus. Cras vitae ligula placerat, aliquam ex vitae, feugiat lectus. Nullam vitae tortor rhoncus, lacinia urna id, semper elit. Sed vel cursus nisi. Mauris eget metus arcu. In velit est, posuere id cursus quis, congue sit amet massa. Sed egestas, massa et vehicula consequat, dolor neque ullamcorper diam, vitae iaculis leo diam sed sapien. Nunc egestas malesuada pretium.</p>
    <p>Morbi quis nulla quam. Duis semper accumsan elit, vel ornare nunc facilisis sed. Ut porttitor lorem ut justo mollis pharetra. Integer finibus vestibulum pulvinar. Quisque sit amet neque sapien. Pellentesque at aliquam erat.</p>
  </div>
  <div class="abs" style="left:35px;top:357px;width:227px;display:flex;justify-content:space-between;font-size:4px;color:var(--ink-soft)">
    <span>www.website.com</span><span>000-000-000</span><span>email@website.com</span>
  </div>
  <div class="abs" style="left:0;top:368px;width:297px;height:17px;background:#c4161c;color:#fff;font-size:4px;text-align:center;line-height:17px">1</div>
</section>

<!-- Service agreement -->
<section class="page" style="left:10px;top:406px">
  <div class="abs" role="img" aria-label="Red-toned photo of a hand signing a document" style="left:0;top:0;width:80px;height:385px;background:linear-gradient(180deg,var(--red-deep) 0%,#c41a20 55%,#d92a2f 100%)"></div>
  <div class="brand on-dark abs" style="left:6px;top:24px;font-size:7.5px">ALPEN COUNSEL</div>
  <div class="abs" style="left:11px;top:344px;font-size:4.3px;line-height:6px;color:#fff">000 – 000 – 000<br>www.website.com<br>email@website.com<br>Address Line 1<br>Address Line 2</div>
  <div class="abs" style="left:91px;top:19px;font-family:Roboto,Arial,sans-serif;font-weight:700;font-size:12.5px;color:var(--red)">SERVICE AGREEMENT</div>
  <div class="body-copy abs" style="left:91px;top:40px;width:199px;font-size:4.1px;line-height:5.9px;text-align:left">
    <p>Lorem ipsum dolor sit amet, consectetur adipiscing elit. Aenean ullamcorper massa volutpat mauris venenatis, non auctor orci varius. Nulla facilisi. Donec placerat accumsan nisi, ac vulputate tellus dapibus tristique. Phasellus ut purus molestie ex molestie elementum vel sit amet urna. Aenean ex nulla, eleifend feugiat facilisis sit amet, consequat ullamcorper orci. Morbi rhoncus ex sit amet sapien commodo.</p>
    <p>Sed congue sed elit id imperdiet. Vestibulum ante ipsum primis in faucibus orci luctus et ultrices posuere cubilia curae; Sed quam tellus, malesuada non lorem ac, luctus hendrerit arcu. Morbi enim ligula, commodo in arcu ut, mollis luctus nisi. Class aptent taciti sociosqu ad litora torquent per conubia nostra.</p>
    <p>Aenean molestie, lacus non maximus ultricies, sapien urna eleifend odio, a ullamcorper urna augue molestie purus. Nulla facilisi. Mauris vel commodo mi. Curabitur volutpat orci a tellus maximus rutrum. Nullam viverra consequat nisl et posuere.</p>
    <p>Morbi quis nulla quam. Duis semper accumsan elit, vel ornare nunc facilisis sed. Ut porttitor lorem ut justo mollis pharetra. Sed congue cursus dolor nec dictum. Integer finibus vestibulum pulvinar. Pellentesque at aliquam erat.</p>
    <p>Cras at justo a diam faucibus finibus. Cras vitae ligula placerat, aliquam ex vitae, feugiat lectus. Nullam vitae tortor rhoncus, lacinia urna id, semper elit. Sed vel cursus nisi. In velit est, posuere id cursus quis, congue sit amet massa. Cras rutrum urna volutpat nulla fringilla, nec sagittis velit congue. Nunc egestas malesuada pretium.</p>
    <p>Morbi quis nulla quam. Duis semper accumsan elit, vel ornare nunc facilisis sed. Ut porttitor lorem ut justo mollis pharetra. Quisque sit amet neque sapien. Pellentesque at aliquam erat.</p>
  </div>
  <div class="abs" style="left:192px;top:342px;width:98px;height:.5px;background:#999"></div>
  <div class="abs" style="left:192px;top:348px;width:98px;text-align:center;font-size:4px">Signature over printed name</div>
  <div class="abs" style="right:7px;top:370px;font-size:4px;color:var(--ink-soft)">pg. 1</div>
</section>

<!-- Tax services -->
<section class="page" style="left:319px;top:406px">
  <div class="map-band" role="img" aria-label="Red band with faint world map" style="top:0;height:29px;background:linear-gradient(180deg,#d81e24,#e53338)"></div>
  <svg class="abs" style="left:0;top:0" width="297" height="385" viewBox="0 0 297 385">
    <polygon points="290,105 263,152 209,152 182,105 209,58 263,58" fill="var(--red)"/>
    <polygon points="330,250 289,321 207,321 166,250 207,179 289,179" fill="var(--grey)"/>
  </svg>
  <svg class="abs" style="left:0;top:0" width="297" height="385" viewBox="0 0 297 385" role="img" aria-label="Photo of a calculator and pen on a financial chart">
    <polygon points="272,199 232,268 152,268 112,199 152,130 232,130" fill="#b9bcc0" stroke="#fff" stroke-width="3"/>
  </svg>
  <div class="hex-title" style="left:17px;top:57px"><b>TAX</b><span>SERVICES</span></div>
  <div class="body-copy abs" style="left:24px;top:88px;width:74px;font-size:3.6px;line-height:5.3px">
    <p>Lorem ipsum dolor sit amet, consectetur adipiscing elit. Aenean ullamcorper massa volutpat mauris venenatis, non auctor orci varius. Nulla facilisi. Donec placerat accumsan nisi, ac vulputate tellus dapibus tristique. Phasellus ut purus molestie ex molestie elementum vel sit amet urna. Aenean ex nulla, eleifend feugiat facilisis sit amet, consequat ullamcorper orci. Morbi rhoncus ex sit amet sapien commodo.</p>
    <p>Curabitur volutpat orci a tellus maximus rutrum. Ut vulputate mi eu leo luctus, et condimentum enim tincidunt. Nullam viverra consequat nisl et posuere. Vestibulum ante ipsum primis in faucibus orci luctus et ultrices posuere cubilia curae;</p>
    <p>Morbi quis nulla quam. Duis semper accumsan elit, vel ornare nunc facilisis sed. Ut porttitor lorem ut justo mollis pharetra. Sed congue cursus dolor nec dictum. Integer finibus vestibulum pulvinar. Ut sed nulla in nisi fermentum luctus. Pellentesque at aliquam erat.</p>
    <p>Cras at justo a diam faucibus finibus. Cras vitae ligula placerat, aliquam ex vitae, feugiat lectus. Nullam vitae tortor</p>
  </div>
  <div class="brand abs" style="left:24px;top:296px;font-size:6.5px;font-weight:600">ALPEN COUNSEL</div>
  <div class="contact-list abs" style="left:24px;top:311px">000 – 000 – 000<br>www.website.com<br>email@website.com<br>Address Line 1<br>Address Line 2</div>
  <div class="abs" role="img" aria-label="Red footer band with faint world map" style="left:0;top:355px;width:297px;height:30px;background:var(--red)"></div>
  <div class="brand on-dark abs" style="right:5px;top:366px;font-size:7.5px">ALPEN COUNSEL</div>
</section>

<!-- Financing -->
<section class="page" style="left:627px;top:406px">
  <div class="map-band" role="img" aria-label="Grey band with faint world map" style="top:0;height:29px;background:linear-gradient(180deg,#5b5c5f,#6a6b6e)"></div>
  <svg class="abs" style="left:0;top:0" width="297" height="385" viewBox="0 0 297 385">
    <polygon points="290,105 263,152 209,152 182,105 209,58 263,58" fill="var(--grey)"/>
    <polygon points="330,250 289,321 207,321 166,250 207,179 289,179" fill="var(--red)"/>
  </svg>
  <svg class="abs" style="left:0;top:0" width="297" height="385" viewBox="0 0 297 385" role="img" aria-label="Photo of a hand stacking coins in rising piles">
    <polygon points="272,199 232,268 152,268 112,199 152,130 232,130" fill="#d9dbdd" stroke="#fff" stroke-width="3"/>
  </svg>
  <div class="hex-title" style="left:18px;top:57px"><b>FINANCING</b></div>
  <div class="body-copy abs" style="left:24px;top:88px;width:74px;font-size:3.6px;line-height:5.3px">
    <p>Lorem ipsum dolor sit amet, consectetur adipiscing elit. Aenean ullamcorper massa volutpat mauris venenatis, non auctor orci varius. Nulla facilisi. Donec placerat accumsan nisi, ac vulputate tellus dapibus tristique. Phasellus ut purus molestie ex molestie elementum vel sit amet urna. Aenean ex nulla, eleifend feugiat facilisis sit amet, consequat ullamcorper orci. Morbi rhoncus ex sit amet sapien commodo.</p>
    <p>Curabitur volutpat orci a tellus maximus rutrum. Ut vulputate mi eu leo luctus, et condimentum enim tincidunt. Nullam viverra consequat nisl et posuere. Vestibulum ante ipsum primis in faucibus orci luctus et ultrices posuere cubilia curae;</p>
    <p>Morbi quis nulla quam. Duis semper accumsan elit, vel ornare nunc facilisis sed. Ut porttitor lorem ut justo mollis pharetra. Sed congue cursus dolor nec dictum. Integer finibus vestibulum pulvinar. Ut sed nulla in nisi fermentum luctus. Pellentesque at aliquam erat.</p>
    <p>Cras at justo a diam faucibus finibus. Cras vitae ligula placerat, aliquam ex vitae, feugiat lectus. Nullam vitae tortor</p>
  </div>
  <div class="brand abs" style="left:24px;top:296px;font-size:6.5px;font-weight:600">ALPEN COUNSEL</div>
  <div class="contact-list abs" style="left:24px;top:311px">000 – 000 – 000<br>www.website.com<br>email@website.com<br>Address Line 1<br>Address Line 2</div>
  <div class="abs" role="img" aria-label="Grey footer band with faint world map" style="left:0;top:355px;width:297px;height:30px;background:var(--grey-dark)"></div>
  <div class="brand on-dark abs" style="right:5px;top:366px;font-size:7.5px">ALPEN COUNSEL</div>
</section>

<!-- Pension plan -->
<section class="page" style="left:10px;top:803px">
  <div class="map-band" role="img" aria-label="Faint dotted world map band" style="top:0;height:29px"></div>
  <div class="map-band" role="img" aria-label="Faint dotted world map band" style="top:356px;height:29px"></div>
  <svg class="abs" style="left:0;top:0" width="297" height="385" viewBox="0 0 297 385">
    <polygon points="292,110 264,158 208,158 180,110 208,62 264,62" fill="var(--grey)"/>
    <polygon points="340,250 290,337 190,337 140,250 190,163 290,163" fill="var(--red)"/>
  </svg>
  <svg class="abs" style="left:0;top:0" width="297" height="385" viewBox="0 0 297 385" role="img" aria-label="Photo of a smiling senior couple embracing outdoors in autumn">
    <polygon points="272,196 232,265 152,265 112,196 152,127 232,127" fill="#c9a453" stroke="#fff" stroke-width="3"/>
  </svg>
  <div class="hex-title" style="left:18px;top:58px"><b>PENSION</b><span>PLAN</span></div>
  <div class="body-copy abs" style="left:24px;top:90px;width:74px;font-size:3.6px;line-height:5.3px">
    <p>Lorem ipsum dolor sit amet, consectetur adipiscing elit. Aenean ullamcorper massa volutpat mauris venenatis, non auctor orci varius. Nulla facilisi. Donec placerat accumsan nisi, ac vulputate tellus dapibus tristique. Phasellus ut purus molestie ex molestie elementum vel sit amet urna. Aenean ex nulla, eleifend feugiat facilisis sit amet, consequat ullamcorper orci. Morbi rhoncus ex sit amet sapien commodo.</p>
    <p>Curabitur volutpat orci a tellus maximus rutrum. Ut vulputate mi eu leo luctus, et condimentum enim tincidunt. Nullam viverra consequat nisl et posuere. Vestibulum ante ipsum primis in faucibus orci luctus et ultrices posuere cubilia curae;</p>
    <p>Morbi quis nulla quam. Duis semper accumsan elit, vel ornare nunc facilisis sed. Ut porttitor lorem ut justo mollis pharetra. Sed congue cursus dolor nec dictum. Integer finibus vestibulum pulvinar. Ut sed nulla in nisi fermentum luctus. Pellentesque at aliquam erat.</p>
    <p>Cras at justo a diam faucibus finibus. Cras vitae ligula placerat, aliquam ex vitae, feugiat lectus. Nullam vitae tortor</p>
  </div>
  <div class="brand abs" style="left:24px;top:295px;font-size:6.5px;font-weight:600">ALPEN COUNSEL</div>
  <div class="contact-list abs" style="left:24px;top:310px">000 – 000 – 000<br>www.website.com<br>email@website.com<br>Address Line 1<br>Address Line 2</div>
  <div class="brand abs" style="right:7px;top:366px;font-size:7.5px">ALPEN COUNSEL</div>
</section>

<!-- Product note -->
<div class="promo">
  <div class="brand">ALPEN COUNSEL</div>
  <div class="promo-line">MS WORD TEMPLATE</div>
  <div class="promo-line">SOURCE FILE INCLUDES</div>
  <div class="promo-line">PDF AND WORD DOCUMENTS</div>
  <div class="promo-line" style="margin-top:6px">THIS IS FOR PREVIEW PURPOSES ONLY</div>
</div>

</body>
</html>
```